依頼詳細
PC版のTOPページと下層1ページ(採用情報)のデザイン制作をお願いいたします。
サイトマップ、依頼内容詳細.txtをご確認いただき、動画のテイストを参考にシンプルで見やすいデザインで制作いただきたいです。
スムーズな連絡と軽微な修正にご対応いただける方へご依頼をさせていただきたいです。
ターゲットは木材資材・建築資材・家具建具資材などを必要とする建築会社様、家具・建具製造会社様などです。
ページ数
2ページ
希望イメージ
シンプル 複雑
単色 カラフル
暗い 明るい
日常 高級
遊び心 厳粛
未来的 伝統的
女性的 男性的
希望する色
茶系、緑系、グレー系
納品ファイル
• イラストレーター形式 (.ai)
補足説明
納品ファイルはXDも可です。
添付してあるアニメーションにテイストを合わせ、
木の温かみを感じさせるデザインで制作してください。
コーポレートですが、あまり堅くなり過ぎないようにしたいです。
BtoB向けの会社ではありますが、就職などを考えている若い方が見ても、
面白そうな企業だなという印象も与えたいです。
動画ダウンロードURLを新たに添付いたしましたので
そちらからダウンロードをお願い致します。
■ 選んだ理由

爽やかな緑を使ったデザインが良かったです。

■ 提案者全員のお礼・コメント

たくさんのご提案をいただきありがとうございました。

```html
<!DOCTYPE html>
<html lang="ja">
<head>
<meta charset="utf-8">
<title>MORIKAZE TIMBER WORKS</title>
<link rel="stylesheet" href="https://fonts.googleapis.com/css2?family=Montserrat:wght@400;500;700&family=Noto+Sans+JP:wght@400;500;700&display=swap">
<style>
:root{
  --ink:#1e1e1e;
  --side:#2a2a2a;
  --bar:#262626;
  --green:#6e9a58;
  --green-dark:#5d8a48;
  --leaf:#7fae5f;
  --grey-light:#dedede;
  --grey-mid:#9a9a9a;
  --white:#ffffff;
  --wood-pale:#e2bd8c;
  --wood-light:#c79a68;
  --wood-mid:#a8744a;
  --wood-dark:#6e4628;
}
*{margin:0;padding:0;box-sizing:border-box}
html,body{width:1200px;height:3132px;overflow:hidden}
body{position:relative;font-family:"Noto Sans JP",sans-serif;color:var(--ink);background:var(--white)}
.abs{position:absolute}

/* sidebar */
.sidebar{left:0;top:0;width:212px;height:2940px;background:var(--side);color:var(--white);z-index:3}
.sidebar .brand{position:absolute;left:22px;top:30px;font-family:"Montserrat",sans-serif;font-weight:500;font-size:26px;line-height:31px}
.nav{position:absolute;top:208px;left:0;width:212px;list-style:none;border-top:1px solid #444}
.nav li{height:62px;line-height:62px;padding-left:46px;font-family:"Montserrat",sans-serif;font-size:12px;border-bottom:1px solid #444}
.nav li.active{background:var(--green)}
.side-links{position:absolute;left:22px;top:594px;font-size:10px;line-height:16px;color:#ccc}

/* top bar */
.topbar{left:212px;top:0;width:988px;height:40px;background:var(--bar);color:#ddd;font-size:11px}
.topbar .tel{position:absolute;right:230px;top:13px}
.topbar .mail{position:absolute;right:40px;top:13px;display:flex;gap:8px;align-items:center}

/* hero */
.hero{left:212px;top:40px;width:988px;height:520px;background:var(--white);overflow:hidden}
.hero-art{position:absolute;inset:0;background:
  radial-gradient(ellipse 190px 230px at 90px 200px,rgba(95,150,70,.75),rgba(95,150,70,.25) 65%,transparent 100%),
  radial-gradient(ellipse 200px 240px at 900px 190px,rgba(95,150,70,.75),rgba(95,150,70,.25) 65%,transparent 100%),
  linear-gradient(90deg,#f3f6ef 0%,#ffffff 30%,#ffffff 70%,#f3f6ef 100%)}
.hero-card{position:absolute;left:262px;top:176px;width:508px;height:186px;background:rgba(85,85,85,.88);border:3px solid #333;color:var(--white);text-align:center}
.hero-card h2{font-family:"Montserrat",sans-serif;font-weight:500;font-size:56px;line-height:64px;margin-top:36px;white-space:nowrap}
.hero-card p{font-family:"Montserrat",sans-serif;font-size:17px;margin-top:4px;white-space:nowrap}
.hero-title{position:absolute;left:170px;top:296px;font-family:"Montserrat",sans-serif;font-weight:500;font-size:74px;line-height:98px;letter-spacing:7px;color:#111;white-space:nowrap}

/* greeting */
.greet-photo{left:212px;top:560px;width:348px;height:320px;background:
  linear-gradient(160deg,rgba(255,255,255,.25) 0%,transparent 35%),
  linear-gradient(100deg,#8a5a34 0%,#c58f5c 22%,#e6c39a 40%,#b5784a 58%,#d9ad7c 74%,#7a4e2e 100%)}
.greet{left:560px;top:560px;width:640px;height:320px;background:var(--green);color:var(--white);padding:40px 30px 0 36px}
.greet h3{font-size:30px;font-weight:400;margin-bottom:14px}
.greet p{font-size:11px;line-height:19px}
.btn-outline{display:block;margin:28px auto 0;width:236px;height:42px;line-height:40px;border:1px solid var(--white);text-align:center;font-size:13px}

/* news */
.news{left:212px;top:880px;width:988px;height:360px;background:var(--grey-light)}
.news-box{position:absolute;left:100px;top:150px;width:120px;height:120px;background:var(--white);border:3px solid #333;text-align:center}
.news-box b{display:block;font-family:"Montserrat",sans-serif;font-weight:500;font-size:28px;margin-top:30px}
.news-box span{font-size:11px}
.news-list{position:absolute;left:320px;top:150px;list-style:none;font-size:11px}
.news-list li{display:flex;align-items:center;height:30px;gap:22px}
.news-list .tag{background:var(--green);color:var(--white);font-size:9px;padding:2px 8px}
.news-bar{left:212px;top:1240px;width:988px;height:50px;background:var(--bar);color:var(--white);text-align:center;line-height:50px;font-size:13px;letter-spacing:2px}

/* product */
.product{left:212px;top:1290px;width:988px;height:570px;background:var(--grey-mid)}
.product-photo{position:absolute;left:0;top:0;width:988px;height:430px;background:
  radial-gradient(ellipse 260px 180px at 660px 90px,rgba(230,200,160,.8),transparent 70%),
  linear-gradient(110deg,#151515 0%,#2e241c 35%,#5a4634 58%,#8a7258 75%,#3a3028 100%)}
.product h3{position:absolute;right:40px;top:48px;font-family:"Montserrat",sans-serif;font-weight:400;font-size:48px;color:var(--white);text-align:right;line-height:54px}
.product h3 small{display:block;font-family:"Noto Sans JP",sans-serif;font-size:14px;line-height:20px}
.tiles{position:absolute;left:0;top:130px;display:flex}
.tile{width:256px;height:300px;position:relative}
.tile .label{position:absolute;left:0;bottom:0;width:100%;height:58px;background:rgba(40,40,40,.6);color:var(--white);font-size:12px;text-align:center;line-height:58px}
.btn-dark{position:absolute;left:340px;top:490px;width:262px;height:46px;line-height:46px;background:var(--bar);color:var(--white);text-align:center;font-size:13px}

/* recruit */
.recruit{left:212px;top:1860px;width:988px;height:580px;background:
  radial-gradient(ellipse 300px 260px at 780px 330px,rgba(235,235,235,.7),transparent 70%),
  linear-gradient(100deg,#2c2c2c 0%,#4e4e4e 30%,#7d7d7d 50%,#bdbdbd 72%,#6a6a6a 100%)}
.recruit-title{position:absolute;left:216px;top:90px;width:150px;height:74px;background:rgba(255,255,255,.88);border:3px solid #444;text-align:center}
.recruit-title b{display:block;font-family:"Montserrat",sans-serif;font-weight:500;font-size:24px;margin-top:8px}
.recruit-title span{font-size:11px}
.recruit p{position:absolute;left:216px;top:180px;width:250px;color:var(--white);font-size:13px;line-height:22px}
.btn-green{position:absolute;left:154px;top:432px;width:208px;height:54px;line-height:54px;background:var(--green);color:var(--white);text-align:center;font-size:14px}

/* contact */
.contact{left:212px;top:2440px;width:988px;height:500px;background:
  linear-gradient(200deg,rgba(255,230,190,.35) 0%,transparent 40%),
  linear-gradient(90deg,#c98d52 0%,#9c6234 22%,#d9a66c 42%,#7d4c28 60%,#b97c46 80%,#6a4022 100%)}
.contact-panel{position:absolute;left:92px;top:64px;width:804px;height:320px;background:rgba(58,58,58,.92);color:var(--white);text-align:center}
.contact-panel h3{font-family:"Montserrat",sans-serif;font-weight:400;font-size:50px;margin-top:18px;line-height:58px}
.contact-panel .lead{font-size:13px;margin-top:2px}
.cards{position:absolute;left:76px;top:136px;display:flex;gap:28px}
.card{width:312px;height:140px;background:var(--white);color:var(--ink);padding-top:16px}
.card .cap{font-size:11px;color:var(--green-dark)}
.card .num{display:flex;justify-content:center;align-items:center;gap:10px;font-family:"Montserrat",sans-serif;font-weight:700;font-size:28px;margin-top:14px}
.card .note{font-size:9px;margin-top:14px;color:#555}
.card .form-btn{display:inline-flex;gap:8px;align-items:center;background:var(--green);color:var(--white);font-size:12px;padding:8px 30px;margin-top:16px}

/* footer */
.foot-left{left:0;top:2940px;width:650px;height:164px;background:var(--grey-light)}
.thumbs{position:absolute;left:278px;top:42px;display:flex;gap:12px}
.thumb{width:84px;height:84px;border:4px solid var(--white);background:radial-gradient(circle at 50% 40%,#9cc47e 0%,#d9e6cf 55%,#f4f4f4 100%)}
.foot-right{left:650px;top:2940px;width:550px;height:164px;background:var(--white)}
.foot-links{position:absolute;top:28px;list-style:none;font-size:11px;line-height:21px}
.copy{left:0;top:3104px;width:1200px;height:28px;background:#111;color:#ccc;font-size:10px;text-align:center;line-height:28px}
</style>
</head>
<body>

<aside class="abs sidebar">
  <div class="brand">MORIKAZE<br>TIMBER<br>WORKS</div>
  <ul class="nav">
    <li>ABOUT US</li>
    <li>PROJECT</li>
    <li>PRODUCT</li>
    <li>CONTACT</li>
    <li class="active">RECRUIT</li>
  </ul>
  <div class="side-links">サイトマップ<br>プライバシーポリシー</div>
</aside>

<header class="abs topbar">
  <span class="tel">TEL：000-000-0000</span>
  <span class="mail">
    <svg width="16" height="12" viewBox="0 0 16 12"><rect x="0.5" y="0.5" width="15" height="11" fill="none" stroke="#ddd"/><path d="M1 1l7 6 7-6" fill="none" stroke="#ddd"/></svg>
    お問い合わせフォーム
  </span>
</header>

<section class="abs hero">
  <div class="hero-art" role="img" aria-label="左右に枝を広げた緑の木々のイラスト"></div>
  <div class="hero-card">
    <h2>lorem ipsum</h2>
    <p>consectetur adipiscing elit,sed do</p>
  </div>
  <h1 class="hero-title">MORIKAZE<br>TIMBER WORKS</h1>
</section>

<div class="abs greet-photo" role="img" aria-label="並べられた木材サンプル板の写真"></div>
<section class="abs greet">
  <h3>ご挨拶</h3>
  <p>ここにダミーテキストが入ります。木材の魅力と確かな品質をお届けするため、私たちは日々取り組んでいます。ここにダミーテキストが入ります。建築会社様、家具・建具製造会社様の良きパートナーとして、一枚一枚の木材と向き合い続けます。ここにダミーテキストが入ります。森の恵みを未来へつなぐために、これからも挑戦を続けてまいります。ここにダミーテキストが入ります。</p>
  <div class="btn-outline">会社情報はこちら</div>
</section>

<section class="abs news">
  <div class="news-box"><b>NEWS</b><span>新着情報</span></div>
  <ul class="news-list">
    <li><span>2021.04.01</span><span class="tag">お知らせ</span><span>新着情報の記事タイトルがここに入ります。</span></li>
    <li><span>2021.04.01</span><span class="tag">お知らせ</span><span>新着情報の記事タイトルがここに入ります。</span></li>
    <li><span>2021.04.01</span><span class="tag">お知らせ</span><span>新着情報の記事タイトルがここに入ります。</span></li>
    <li><span>2021.04.01</span><span class="tag">お知らせ</span><span>新着情報の記事タイトルがここに入ります。</span></li>
  </ul>
</section>
<div class="abs news-bar">新着情報一覧を見る</div>

<section class="abs product">
  <div class="product-photo" role="img" aria-label="作業台に置かれた木材の写真"></div>
  <h3>PRODUCT<small>取扱商品</small></h3>
  <div class="tiles">
    <div class="tile" role="img" aria-label="明るい木目の商品写真" style="background:linear-gradient(95deg,#d9b07e 0%,#eccb9f 30%,#c99b68 55%,#e3bd8d 80%,#c69462 100%)"><div class="label">商品名</div></div>
    <div class="tile" role="img" aria-label="木目の商品写真" style="background:linear-gradient(85deg,#a8724a 0%,#c9966a 25%,#8f5e3a 50%,#c28c5e 75%,#9c6a44 100%)"><div class="label">商品名</div></div>
    <div class="tile" role="img" aria-label="木目の商品写真" style="background:linear-gradient(100deg,#c08a58 0%,#dcae7a 30%,#b27a4a 60%,#d4a170 100%)"><div class="label">商品名</div></div>
  </div>
  <div class="btn-dark">取扱商品一覧を見る</div>
</section>

<section class="abs recruit" role="img" aria-label="木の床で働く人々の足元の写真">
  <div class="recruit-title"><b>RECRUIT</b><span>採用情報</span></div>
  <p>これはダミーテキストです。私たちと一緒に木の仕事に挑戦しませんか。これはダミーテキストです。若い力を歓迎しています。これはダミーテキストです。</p>
  <div class="btn-green">採用情報を見る</div>
</section>

<section class="abs contact" role="img" aria-label="並んだ木材の写真">
  <div class="contact-panel">
    <h3>CONTACT</h3>
    <div class="lead">まずはお気軽にお問い合わせ下さい。</div>
    <div class="cards">
      <div class="card">
        <div class="cap">お電話でのお問い合わせは</div>
        <div class="num">
          <svg width="26" height="26" viewBox="0 0 26 26"><circle cx="13" cy="13" r="13" fill="#6e9a58"/><path d="M9 7l3 3-1.5 2a8 8 0 0 0 4 4l2-1.5 3 3-2 2C12 19 7 14 7 9z" fill="#fff"/></svg>
          000-000-0000
        </div>
        <div class="note">受付時間 9:00〜18:00（土日祝除く）</div>
      </div>
      <div class="card">
        <div class="cap">WEBからのお問い合わせは</div>
        <div class="form-btn">
          <svg width="14" height="10" viewBox="0 0 14 10"><rect x="0.5" y="0.5" width="13" height="9" fill="none" stroke="#fff"/><path d="M1 1l6 5 6-5" fill="none" stroke="#fff"/></svg>
          お問い合わせフォーム
        </div>
        <div class="note">24時間受付・翌営業日に返信いたします。</div>
      </div>
    </div>
  </div>
</section>

<footer>
  <div class="abs foot-left">
    <div class="thumbs">
      <div class="thumb" role="img" aria-label="木のイラスト"></div>
      <div class="thumb" role="img" aria-label="木のイラスト"></div>
      <div class="thumb" role="img" aria-label="木のイラスト"></div>
    </div>
  </div>
  <div class="abs foot-right">
    <ul class="foot-links" style="left:30px">
      <li>会社概要</li><li>事業内容</li><li>取扱商品</li><li>メーカーリンク集</li><li>お問合せフォーム</li>
    </ul>
    <ul class="foot-links" style="left:240px">
      <li>新着情報一覧</li><li>採用情報</li><li>会社情報</li><li>プライバシーポリシー</li><li>サイトマップ</li>
    </ul>
  </div>
  <div class="abs copy">Copyright © 2021 森風木材株式会社 All Rights Reserved.</div>
</footer>

</body>
</html>
```